Simple graphic for a book or slide presentation

We are looking for a style that suits the style of our book. It's title is Venture. Thriving boldly on uncertain ground. There will be more line drawing/graphics in the book but how you design this image will create the style for all the other simple graphics in the book (once we decide what they are). So this one design will lead to a few more to match the style of this one. We'd like the shape of the overall graphic (i.e the arrows and words/bubbles) to be circular (not a rounded square as appears in the sample attached). Perhaps the words don't need to be in ovals or bound by anything at all; perhaps they do - let's see what you see. We'd like you to choose a font or offer many different fonts you think will capture the practical yet unconventional tone of the book. The book is teaching that managing risks in life is a life-skill that can be learned. The section of the book where this graphic will be placed is called "the power of language" - basically we are saying that thoughts, words and actions create our culture and our destiny. This insight comes from Pranav Kelkari's famous quote:
Carefully watch your thoughts, for they become your words.
Manage and watch your words, for they will become your actions.
Consider and judge your actions, for they have become your habits.
Acknowledge and watch your habits, for they shall become your values.
Understand and embrace your values, for they become your destiny.

Please change the text in the middle of the graphic to say: The Human Culture Cycle

```html
<!DOCTYPE html>
<html lang="en">
<head>
<meta charset="utf-8">
<title>The Human Culture Cycle</title>
<link rel="stylesheet" href="https://fonts.googleapis.com/css2?family=Fira+Sans:wght@300;600&display=swap">
<style>
  :root {
    --bg-top: #d2d2d2;
    --bg-bottom: #ffffff;
    --disc: #d7e021;
    --label: #0a72bd;
    --label-text: #ffffff;
    --title-text: #231f20;
    --arrow: #555555;
    --fold-dark: #8c8c8c;
    --fold-light: #e6e6e6;
  }
  html, body {
    margin: 0;
    padding: 0;
    width: 1200px;
    height: 1137px;
    overflow: hidden;
  }
  body {
    background: linear-gradient(to bottom, var(--bg-top) 0%, var(--bg-bottom) 62%, var(--bg-bottom) 100%);
  }
  .cycle-graphic {
    display: block;
    width: 1200px;
    height: 1137px;
  }
  .cycle-disc { fill: var(--disc); }
  .stage-box { fill: var(--label); }
  .stage-fold { fill: url(#foldShade); }
  .stage-label {
    font-family: "Fira Sans", Arial, sans-serif;
    font-weight: 300;
    font-size: 46px;
    fill: var(--label-text);
    text-anchor: middle;
  }
  .cycle-title {
    font-family: "Fira Sans", Arial, sans-serif;
    font-weight: 600;
    font-size: 41px;
    fill: var(--title-text);
    text-anchor: middle;
  }
  .flow-arrow {
    fill: none;
    stroke: var(--arrow);
    stroke-width: 1.8;
    stroke-dasharray: 6 5;
  }
  .arrow-head {
    fill: none;
    stroke: var(--arrow);
    stroke-width: 1.8;
  }
</style>
</head>
<body>
<svg class="cycle-graphic" viewBox="0 0 950 900" xmlns="http://www.w3.org/2000/svg">
  <defs>
    <linearGradient id="foldShade" x1="0" y1="0" x2="1" y2="0">
      <stop offset="0" stop-color="var(--fold-dark)"/>
      <stop offset="0.5" stop-color="var(--fold-light)"/>
      <stop offset="1" stop-color="var(--fold-dark)"/>
    </linearGradient>
    <marker id="arrowTip" viewBox="0 0 10 10" refX="8" refY="5" markerWidth="9" markerHeight="9" orient="auto">
      <path class="arrow-head" d="M1,1 L8,5 L1,9"/>
    </marker>
  </defs>

  <circle class="cycle-disc" cx="473" cy="447" r="316"/>

  <g class="cycle-title">
    <text x="473" y="428">The Human</text>
    <text x="473" y="490">Culture Cycle</text>
  </g>

  <g class="flow-arrows">
    <path class="flow-arrow" marker-end="url(#arrowTip)" d="M606,140 A340,340 0 0 1 748,250"/>
    <path class="flow-arrow" marker-end="url(#arrowTip)" d="M795,330 A340,340 0 0 1 805,535"/>
    <path class="flow-arrow" marker-end="url(#arrowTip)" d="M750,648 A340,340 0 0 1 592,766"/>
    <path class="flow-arrow" marker-end="url(#arrowTip)" d="M357,768 A340,340 0 0 1 200,654"/>
    <path class="flow-arrow" marker-end="url(#arrowTip)" d="M153,566 A340,340 0 0 1 145,366"/>
    <path class="flow-arrow" marker-end="url(#arrowTip)" d="M196,252 A340,340 0 0 1 325,146"/>
  </g>

  <g class="stage stage-thoughts">
    <rect class="stage-fold" x="327" y="107" width="34" height="38" rx="5"/>
    <rect class="stage-fold" x="588" y="107" width="34" height="44" rx="5"/>
    <rect class="stage-box" x="350" y="107" width="248" height="70" rx="8"/>
    <text class="stage-label" x="474" y="158">Thoughts</text>
  </g>

  <g class="stage stage-words">
    <rect class="stage-fold" x="780" y="318" width="44" height="42" rx="5"/>
    <rect class="stage-box" x="647" y="254" width="177" height="70" rx="8"/>
    <text class="stage-label" x="735" y="305">Words</text>
  </g>

  <g class="stage stage-actions">
    <rect class="stage-fold" x="770" y="540" width="54" height="44" rx="5"/>
    <rect class="stage-box" x="619" y="578" width="205" height="70" rx="8"/>
    <text class="stage-label" x="721" y="629">Actions</text>
  </g>

  <g class="stage stage-habits">
    <rect class="stage-fold" x="359" y="745" width="34" height="48" rx="5"/>
    <rect class="stage-fold" x="556" y="745" width="34" height="48" rx="5"/>
    <rect class="stage-box" x="384" y="722" width="182" height="68" rx="8"/>
    <text class="stage-label" x="475" y="772">Habits</text>
  </g>

  <g class="stage stage-values">
    <rect class="stage-fold" x="125" y="540" width="58" height="44" rx="5"/>
    <rect class="stage-box" x="125" y="577" width="182" height="71" rx="8"/>
    <text class="stage-label" x="216" y="629">Values</text>
  </g>

  <g class="stage stage-culture">
    <rect class="stage-fold" x="125" y="318" width="58" height="42" rx="5"/>
    <rect class="stage-box" x="125" y="254" width="198" height="70" rx="8"/>
    <text class="stage-label" x="224" y="305">Culture</text>
  </g>
</svg>
</body>
</html>
```